Electrical Safety Inspection for High End Customers

Flyer designed to advertise a 50 point electrical safety check service available from a recent start up electrician's firm in Auckland, New Zealand. I am a registered electrical inspector with 16 years experience.
Targeting high end customers, so I want the flyer to have a premium feel to it (glossy black background, etc). The final design should communicate peace of mind. The price will be $60 incl. GST
The checks included should be 1) Mains Cable 2)Mains entry point 3)Switchboard 4)Circuit protection correctly rated 5)Circuit protection operational 6)The main earthing system 7)Safety systems 8)Light fittings 9)Socket outlets 10)Deterioration of fittings 11)Deterioration of cabling 12)Compliance with current regulations
I have included a copy of the test sheet for reference. I have also included my logo and the senior circuitry federation of New Zealand, both of which must be present.
Target Market(s)
High end home owners
Industry/Entity Type
Electrician
Colors
Designer to choose colors to be used in the design.
Look and feel

```html
<!DOCTYPE html>
<html lang="en">
<head>
<meta charset="utf-8">
<title>50 Point Electrical Safety Check Service – Flyer</title>
<link rel="stylesheet" href="https://fonts.googleapis.com/css2?family=Oswald:wght@500;600;700&family=Montserrat:wght@500;600;700;800&display=swap">
<style>
  :root{
    --ink:#111114;
    --night:#0d0d12;
    --night-soft:#1d1f29;
    --brand-red:#e31b23;
    --brand-blue:#1474c4;
    --paper:#ffffff;
    --backdrop:#e6e6e8;
    --muted:#55565c;
  }
  *{box-sizing:border-box;margin:0;padding:0}
  html,body{width:1200px;height:849px;overflow:hidden;background:var(--backdrop)}
  body{font-family:"Montserrat",Arial,sans-serif;position:relative}
  .flyer{position:absolute;left:317px;top:24px;width:566px;height:800px;background:var(--paper);overflow:hidden;box-shadow:0 6px 24px rgba(0,0,0,.18)}

  /* brand */
  .brand{position:absolute;left:22px;top:92px;display:flex;align-items:center;gap:8px}
  .brand-dot{width:30px;height:30px;border-radius:50%;background:var(--ink)}
  .brand-name{font-weight:800;font-size:17px;line-height:1;color:var(--ink);letter-spacing:.5px}

  /* headline */
  .headline{position:absolute;right:24px;top:14px;width:320px}
  .headline-top{display:flex;align-items:flex-end;gap:8px;font-family:"Oswald",Arial,sans-serif;font-weight:700;color:var(--ink);line-height:.85}
  .headline-number{font-size:96px;letter-spacing:-4px;display:flex;align-items:flex-end}
  .headline-number svg{width:56px;height:74px;margin-bottom:4px}
  .headline-point{font-size:64px;letter-spacing:-1px}
  .headline-rule{height:2px;background:#bdbdc2;margin:6px 0 4px}
  .headline-service{font-family:"Oswald",Arial,sans-serif;font-weight:700;color:var(--brand-red);font-size:34px;line-height:1.02;text-transform:uppercase;text-align:right}
  .headline-city{margin-top:5px;border-top:2px solid #bdbdc2;padding-top:4px;font-weight:800;font-size:11px;letter-spacing:.5px;color:var(--ink);text-align:right}

  /* dark showcase */
  .showcase-bg{position:absolute;left:0;top:262px;width:566px;height:444px;background:radial-gradient(ellipse at 70% 40%,var(--night-soft),var(--night) 70%)}
  .credentials{position:absolute;left:300px;top:224px;width:266px;height:84px;background:var(--brand-blue);padding:9px 12px 0 36px}
  .credentials li{list-style:none;color:#fff;font-weight:600;font-size:10.5px;line-height:1.15;margin-bottom:5px;position:relative}
  .credentials li::before{content:"";position:absolute;left:-14px;top:3px;width:6px;height:6px;border-radius:50%;background:#fff}

  .hero-photo{position:absolute;left:12px;top:200px;width:316px;height:286px}
  .detail-photos{position:absolute;left:318px;top:318px;width:240px;height:200px}

  .price{position:absolute;right:10px;top:448px;color:#fff;text-align:right;white-space:nowrap}
  .price-amount{font-family:"Oswald",Arial,sans-serif;font-weight:600;font-size:22px;line-height:1}
  .price-note{font-weight:600;font-size:8px;letter-spacing:.5px}

  /* checks */
  .checks-tag{position:absolute;left:18px;top:500px;background:var(--brand-blue);color:#fff;font-weight:800;font-size:16px;padding:5px 22px 5px 12px;clip-path:polygon(0 0,100% 0,90% 100%,0 100%)}
  .checks{position:absolute;display:flex;flex-direction:column;gap:7px}
  .checks-left{left:26px;top:542px}
  .checks-right{left:300px;top:530px}
  .check{display:flex;align-items:flex-start;gap:7px;color:#fff;font-weight:600;font-size:10.5px;line-height:1.15;text-transform:uppercase;width:230px}
  .check svg{flex:none;width:12px;height:12px}

  /* band */
  .tagline{position:absolute;left:0;top:706px;width:566px;height:22px;background:var(--brand-blue);color:#fff;font-weight:800;font-size:12.5px;letter-spacing:.4px;padding:4px 0 0 168px;white-space:nowrap}

  /* footer */
  .enquire{position:absolute;left:22px;top:714px;width:124px;height:80px;background:var(--brand-red);color:#fff;font-weight:500;font-size:12.5px;line-height:1.2;padding:14px 10px 0 12px;text-transform:uppercase}
  .contact{position:absolute;left:156px;top:738px}
  .contact-row{display:flex;align-items:center;gap:8px}
  .contact-phone{font-family:"Oswald",Arial,sans-serif;font-weight:600;font-size:22px;color:var(--ink);line-height:1;white-space:nowrap}
  .contact-lines{font-weight:700;font-size:9.5px;color:var(--ink);line-height:1.35}
  .contact-icon{width:20px;height:20px;flex:none}
  .divider{position:absolute;top:740px;width:1px;height:48px;background:#c9c9ce}
  .social{position:absolute;left:352px;top:744px;width:62px;display:flex;flex-direction:column;align-items:center}
  .social-label{font-weight:600;font-size:7px;color:var(--muted);line-height:1.2;text-align:center}
  .social-dots{display:flex;gap:4px;margin-top:4px}
  .social-dots span{width:15px;height:15px;border-radius:50%;background:var(--ink)}
  .badges{position:absolute;left:430px;top:746px;display:flex;align-items:center;gap:10px}
  .badge-federation{width:70px;height:30px;background:#eef3fa;border:2px solid var(--brand-blue);border-radius:3px}
  .badge-inspectors{width:34px;height:34px;border-radius:50%;border:2px solid var(--ink)}
</style>
</head>
<body>
<main class="flyer">

  <div class="showcase-bg" role="img" aria-label="Darkened photo of a switchboard with wiring"></div>

  <div class="brand">
    <span class="brand-dot"></span>
    <span class="brand-name">KOWHAI LINE<br>ELECTRICAL</span>
  </div>

  <header class="headline">
    <div class="headline-top">
      <span class="headline-number">5<svg viewBox="0 0 62 82" aria-hidden="true"><ellipse cx="31" cy="41" rx="25" ry="34" fill="none" stroke="#111114" stroke-width="11"/><path d="M16 42 L28 56 L52 20" fill="none" stroke="#e31b23" stroke-width="8" stroke-linecap="round" stroke-linejoin="round"/></svg></span>
      <span class="headline-point">POINT</span>
    </div>
    <div class="headline-rule"></div>
    <h1 class="headline-service">Electrical Safety<br>Check Service</h1>
    <p class="headline-city">AVAILABLE IN YOUR CITY</p>
  </header>

  <ul class="credentials">
    <li>16 YEARS EXPERIENCE</li>
    <li>FULLY REGISTERED<br>ELECTRICAL INSPECTOR</li>
    <li>PROFESSIONALISM,<br>EXPERTISE AND EFFICIENCY</li>
  </ul>

  <svg class="hero-photo" viewBox="0 0 320 290">
    <defs>
      <linearGradient id="heroFill" x1="0" y1="0" x2="1" y2="1">
        <stop offset="0" stop-color="#8d97a6"/>
        <stop offset=".5" stop-color="#c9463f"/>
        <stop offset="1" stop-color="#3b4c7a"/>
      </linearGradient>
    </defs>
    <polygon points="80,4 240,4 316,145 240,286 80,286 4,145" fill="#e31b23"/>
    <polygon points="88,20 232,20 298,145 232,270 88,270 22,145" fill="url(#heroFill)" role="img" aria-label="Photo of an electrician testing a switchboard with a multimeter"/>
  </svg>

  <svg class="detail-photos" viewBox="0 0 240 200">
    <defs>
      <linearGradient id="gloveFill" x1="0" y1="0" x2="1" y2="1"><stop offset="0" stop-color="#c9b79a"/><stop offset="1" stop-color="#b23a34"/></linearGradient>
      <linearGradient id="planFill" x1="0" y1="0" x2="1" y2="1"><stop offset="0" stop-color="#e6e2da"/><stop offset="1" stop-color="#6c5a48"/></linearGradient>
      <linearGradient id="workFill" x1="0" y1="0" x2="1" y2="1"><stop offset="0" stop-color="#d49b6a"/><stop offset="1" stop-color="#5b3c2c"/></linearGradient>
    </defs>
    <polygon points="28,2 82,2 108,48 82,94 28,94 2,48" fill="none" stroke="#fff" stroke-width="2"/>
    <polygon points="31,8 79,8 101,48 79,88 31,88 9,48" fill="url(#gloveFill)" role="img" aria-label="Photo of gloved hands stripping wires"/>
    <polygon points="156,2 210,2 236,48 210,94 156,94 130,48" fill="none" stroke="#fff" stroke-width="2"/>
    <polygon points="159,8 207,8 229,48 207,88 159,88 137,48" fill="url(#planFill)" role="img" aria-label="Photo of hands reviewing electrical plans on a desk"/>
    <polygon points="92,102 146,102 172,148 146,194 92,194 66,148" fill="none" stroke="#fff" stroke-width="2"/>
    <polygon points="95,108 143,108 165,148 143,188 95,188 73,148" fill="url(#workFill)" role="img" aria-label="Photo of an electrician at work"/>
  </svg>

  <div class="price">
    <div class="price-amount">$60 GST</div>
    <div class="price-note">INCLUDED</div>
  </div>

  <h2 class="checks-tag">CHECKS INCLUDED</h2>

  <ul class="checks checks-left">
    <li class="check"><svg viewBox="0 0 12 12"><circle cx="6" cy="6" r="6" fill="#1474c4"/><path d="M3 6.2 L5.2 8.3 L9 3.8" fill="none" stroke="#fff" stroke-width="1.6"/></svg>Mains cable</li>
    <li class="check"><svg viewBox="0 0 12 12"><circle cx="6" cy="6" r="6" fill="#1474c4"/><path d="M3 6.2 L5.2 8.3 L9 3.8" fill="none" stroke="#fff" stroke-width="1.6"/></svg>Mains entry point</li>
    <li class="check"><svg viewBox="0 0 12 12"><circle cx="6" cy="6" r="6" fill="#1474c4"/><path d="M3 6.2 L5.2 8.3 L9 3.8" fill="none" stroke="#fff" stroke-width="1.6"/></svg>Switchboard</li>
    <li class="check"><svg viewBox="0 0 12 12"><circle cx="6" cy="6" r="6" fill="#1474c4"/><path d="M3 6.2 L5.2 8.3 L9 3.8" fill="none" stroke="#fff" stroke-width="1.6"/></svg>Circuit protection<br>correctly rated</li>
    <li class="check"><svg viewBox="0 0 12 12"><circle cx="6" cy="6" r="6" fill="#1474c4"/><path d="M3 6.2 L5.2 8.3 L9 3.8" fill="none" stroke="#fff" stroke-width="1.6"/></svg>Circuit protection<br>operational</li>
    <li class="check"><svg viewBox="0 0 12 12"><circle cx="6" cy="6" r="6" fill="#1474c4"/><path d="M3 6.2 L5.2 8.3 L9 3.8" fill="none" stroke="#fff" stroke-width="1.6"/></svg>The main earthing<br>system</li>
  </ul>

  <ul class="checks checks-right">
    <li class="check"><svg viewBox="0 0 12 12"><circle cx="6" cy="6" r="6" fill="#1474c4"/><path d="M3 6.2 L5.2 8.3 L9 3.8" fill="none" stroke="#fff" stroke-width="1.6"/></svg>Safety systems</li>
    <li class="check"><svg viewBox="0 0 12 12"><circle cx="6" cy="6" r="6" fill="#1474c4"/><path d="M3 6.2 L5.2 8.3 L9 3.8" fill="none" stroke="#fff" stroke-width="1.6"/></svg>Light fittings</li>
    <li class="check"><svg viewBox="0 0 12 12"><circle cx="6" cy="6" r="6" fill="#1474c4"/><path d="M3 6.2 L5.2 8.3 L9 3.8" fill="none" stroke="#fff" stroke-width="1.6"/></svg>Socket outlets</li>
    <li class="check"><svg viewBox="0 0 12 12"><circle cx="6" cy="6" r="6" fill="#1474c4"/><path d="M3 6.2 L5.2 8.3 L9 3.8" fill="none" stroke="#fff" stroke-width="1.6"/></svg>Deterioration of<br>fittings</li>
    <li class="check"><svg viewBox="0 0 12 12"><circle cx="6" cy="6" r="6" fill="#1474c4"/><path d="M3 6.2 L5.2 8.3 L9 3.8" fill="none" stroke="#fff" stroke-width="1.6"/></svg>Deterioration of<br>cabling</li>
    <li class="check"><svg viewBox="0 0 12 12"><circle cx="6" cy="6" r="6" fill="#1474c4"/><path d="M3 6.2 L5.2 8.3 L9 3.8" fill="none" stroke="#fff" stroke-width="1.6"/></svg>Compliance with<br>current regulations</li>
  </ul>

  <div class="tagline">LEADERS IN ELECTRICAL DESIGN AND INSTALLATION</div>

  <div class="enquire">For more<br>inspections<br>call or visit</div>

  <div class="contact">
    <div class="contact-row">
      <svg class="contact-icon" viewBox="0 0 22 22"><circle cx="11" cy="11" r="11" fill="#e31b23"/><path d="M7.5 6 L9.5 6 L10.3 8.6 L9 9.6 Q10.2 12 12.4 13 L13.4 11.7 L16 12.5 L16 14.5 Q15.5 16 13.8 16 Q7.5 15 6 8.2 Q6 6.5 7.5 6 Z" fill="#fff"/></svg>
      <span class="contact-phone">64 027 555 0148</span>
    </div>
    <div class="contact-row" style="margin-top:7px">
      <svg class="contact-icon" viewBox="0 0 22 22"><circle cx="11" cy="11" r="11" fill="#e31b23"/><circle cx="11" cy="11" r="6" fill="none" stroke="#fff" stroke-width="1.4"/><ellipse cx="11" cy="11" rx="2.6" ry="6" fill="none" stroke="#fff" stroke-width="1.2"/><path d="M5 11 H17" stroke="#fff" stroke-width="1.2"/></svg>
      <span class="contact-lines">www.kowhailine.co.nz<br>hello@kowhailine.co.nz</span>
    </div>
  </div>

  <div class="divider" style="left:345px"></div>
  <div class="social">
    <div class="social-label">GET SOCIAL<br>WITH US</div>
    <div class="social-dots"><span></span><span></span><span></span></div>
  </div>
  <div class="divider" style="left:421px"></div>

  <div class="badges">
    <div class="badge-federation" role="img" aria-label="Senior circuitry federation of New Zealand membership badge"></div>
    <div class="badge-inspectors" role="img" aria-label="Inspectors association badge"></div>
  </div>

</main>
</body>
</html>
```